Transform Wine Label to Pavel Runoski Style

The task involves transforming a wine label into the iconic visual style of Pavel Runoski while keeping the image's content intact. The goal is to create a luxurious and Old-World elegant label that reflects the essence of Runoski's artistic style.

Specifications:
The design should modify the visual elements such as color saturation, line clarity, and overall style to resemble Pavel Runoski's signature artistic approach.
The content of the original image, including its shape and subject matter, should remain unchanged.
The label should have a standard square shape, appropriate for a wine bottle, with the map of France found within its borders.
The lettering on the label should be in gold, with the words "בלווני" (meaning France) and "Belvoni" (brand name) positioned below the first word.
The overall feel of the label should exude luxury and reflect the elegance of the Old-World.

Guidelines:
Submit your design entries in high-resolution formats compatible with printing, such as PDF, PNG, or JPEG.
Ensure that your design accurately captures the unique artistic style and aesthetic of Pavel Runoski while maintaining the original image's content.
Take inspiration from Runoski's use of vibrant colors, dreamlike elements, and emotional associations in your design.
Consider incorporating Runoski's narrative and symbolic themes, taking into account his Jewish heritage and occasional use of Christian imagery.
Make use of gold lettering to enhance the luxurious feel of the label.

Important Note:
All design entries must be original and free from any copyright infringement.
By submitting your designs, you agree to transfer the ownership rights to the contest holder upon winning.

Sick

```html
<!DOCTYPE html>
<html lang="en">
<head>
<meta charset="utf-8">
<title>Belvoni Wine Label</title>
<link rel="stylesheet" href="https://fonts.googleapis.com/css2?family=Frank+Ruhl+Libre:wght@500&display=swap">
<style>
  :root {
    --backdrop: #f9c350;
    --silver-light: #eef0f0;
    --silver-mid: #c9cccd;
    --silver-dark: #b4b8b9;
    --gold-text: #8a7048;
    --gold-mid: #b8975e;
    --gold-light: #e2c98f;
    --frame-gold: #c3a878;
  }
  html, body {
    margin: 0;
    padding: 0;
    width: 1200px;
    height: 901px;
    overflow: hidden;
    background: var(--backdrop);
  }
  .canvas {
    position: relative;
    width: 1200px;
    height: 901px;
  }
  .label {
    position: absolute;
    left: 220px;
    top: 35px;
    width: 760px;
    height: 830px;
    background: linear-gradient(90deg,
      var(--silver-dark) 0%,
      var(--silver-mid) 18%,
      var(--silver-light) 42%,
      var(--silver-mid) 68%,
      var(--silver-dark) 100%);
  }
  .label-frame {
    position: absolute;
    left: 22px;
    top: 22px;
    right: 22px;
    bottom: 22px;
    border: 2px solid var(--frame-gold);
  }
  .map-illustration {
    position: absolute;
    left: 94px;
    top: 140px;
    width: 376px;
    height: 380px;
    border-radius: 42% 38% 46% 40%;
    background: radial-gradient(circle at 45% 45%,
      #c0345e 0%, #7d4fa0 30%, #3f9fb6 55%, #6fbf4a 75%, #e0b24a 100%);
  }
  .ornament-band {
    position: absolute;
    left: 626px;
    top: 24px;
    width: 104px;
    height: 766px;
    background: linear-gradient(180deg, var(--gold-light), var(--gold-mid), var(--gold-light));
    opacity: 0.85;
  }
  .name-hebrew,
  .brand-name {
    position: absolute;
    right: 172px;
    margin: 0;
    font-family: "Frank Ruhl Libre", serif;
    font-weight: 500;
    line-height: 1;
    color: var(--gold-text);
  }
  .name-hebrew {
    top: 590px;
    font-size: 54px;
    direction: rtl;
  }
  .brand-name {
    top: 668px;
    font-size: 92px;
    letter-spacing: 1px;
  }
</style>
</head>
<body>
  <main class="canvas">
    <section class="label">
      <div class="label-frame"></div>
      <div class="map-illustration" role="img" aria-label="Colourful dreamlike painted map of France"></div>
      <div class="ornament-band" role="img" aria-label="Vertical gold decorative pattern band"></div>
      <p class="name-hebrew" lang="he">בלווני</p>
      <h1 class="brand-name">BELVONI</h1>
    </section>
  </main>
</body>
</html>
```